Trade Show Package: Logo, B. Card, Brochure, T Shirt & Signs

We have a trade show coming up and will need the following designed: tri-fold, logo cleanup, business cards, t-shirt text and 6 poster signs.

We want all our materials to be consistent, modern (san serif fonts) contemporary and clean. You can take a look at our website, www.bright-lane-webworks.com to see the color scheme we are using and overall look (we use dark red, grey, black, charcoal grey).

1- Logo Cleanup
Our logo is attached. It needs to be cleaned up and sharp so that it looks really good on all of our materials.
We need a thin red line added to the bottom of the logo. See the logo on the tri-fold on the bottom right.
Perhaps the tagline, business on skyforge88 should be a lighter charcoal grey.

If you have any ideas that you think would make it better, of course we welcome that.

We need the logo cleaned up first as the logo is needed for the business cards, tri-fold, t-shirts and signs.

2- Business Cards
Our business cards will be printed on white paper.
Top has a dark red border, followed by our logo (with thin red line underneath) followed by text.

Here is a screencast of what we are going for: http://clipvault-demo.net/t/QxR7p2kWdnLa
We'll need the two separate cards shown in the screencast.

BASIC STYLE: clean, modern design

FONT: modern, easy to read

COLORS: dark red for the bar at the top (full bleed) and Marcus's name & possibly charcoal grey for the rest of the text

3- Tri-fold
3 (5x7 panels) brochure

This brochure is all about cloud computing. I have attached a plain pdf that I put together just to show the order of the tri-fold; this is not the design we
want, we want a modern design, clean, consistent colors and look.

We have 2 pictures we found but if you think another picture would work better for the design, please
show us your ideas.

Here is what we are looking for:

COLOR: will be printed on white paper, except one page will be black (testimonials page, full bleed);
also we need to have a spot uv on the front and back covers and we want a font that does well with that. The video with the black brochure will show the spot uv we are looking for.

BASIC STYLE: clean, modern and innovative

FONT: modern, easy to read and shows up well on paper (san serif fonts)

Left inside trifold: man in a brown box working - see link I provided at the bottom of that page; let me know the size you require and I'll purchase it and email it to you. We want this page to match or complement the coloring of the rest of our brochure, maybe something like this (reddish overtones? instead of the brown which doesn't go). Picture full bleed.

Middle inside: man lying on grass, dreaming of bubble - see link I provided at the bottom of that page; let me know the size you require and I'll purchase it and email it to you. Picture full bleed.

Right inside: text (boost business with cloud computing) with our logo on the bottom right (the word "might" needs to be in italics)

Outside left: the testimonials goes here, make background black (this page only) with white or other light text, full black bleed

Outside middle: BACK COVER - our logo and address

Outside right: FRONT COVER - text (get your cloud on) and our logo on bottom right (with the thin red line underneath)

4- Shirts
T-SHIRT FRONT: our logo on left side

T-SHIRT BACK:
Ask Me (should be biggest font size and in red)
about (should be on second line and smaller in black)
Cloud Computing (should be on the third line, black text and smaller than ask me but big)

- find a graphical element from our logo and use it here, for example the red line, to make it easier to read and make it interesting
- should be modern (consistent with the rest of our materials, i.e. brochure ...)
- attached a sample look we put together but we need a designed modern look

5- Signs
Here is a preliminary look at our signs (pdf attached), last 2 slides will be updated slightly and sent back to you with dimensions for all the signs.

Text should be 1 1/2 inches from the frames border. Will be printed on a white background.

BASIC STYLE: clean, modern design (something that will draw people to look at the sign)
the thick red rectangle on the bottom with the logo on the right should be more interesting, maybe add gradient, texture, etc.

FONT: modern, easy to read (san serif fonts) first 4 posters should be the same exact font and size.

COLORS: dark red, black, greys, charcoal grey

NOTE: We will only guarantee payment once we see designs that match our criteria. We cannot guarantee until we have SEEN your work.

```html
<!DOCTYPE html>
<html lang="en">
<head>
<meta charset="utf-8">
<title>Bright-Lane-Webworks — Tri-fold Inside Spread</title>
<link rel="stylesheet" href="https://fonts.googleapis.com/css2?family=Open+Sans:wght@400;600;700&family=Titillium+Web:wght@300;400;600;700&display=swap">
<style>
  :root {
    --dark-red: #a3201c;
    --brand-red: #b0221d;
    --charcoal: #3a3a3a;
    --body-grey: #8a8a8a;
    --rule-grey: #d6d6d6;
    --frame-grey: #e1e1e1;
    --paper: #ffffff;
    --sepia-light: #a8988a;
    --sepia-mid: #6b5a4c;
    --sepia-dark: #231b16;
    --sky-light: #d8d3cd;
    --sky-mid: #8f877f;
    --grass-dark: #1f1b18;
  }
  * { margin: 0; padding: 0; box-sizing: border-box; }
  html, body {
    width: 1200px; height: 900px; overflow: hidden;
    background: var(--paper);
  }
  .canvas { position: relative; width: 1200px; height: 900px; }

  .spread {
    position: absolute; left: 37px; top: 187px;
    width: 1126px; height: 524px;
    border: 1px solid var(--frame-grey);
  }
  .panel { position: absolute; top: 0; height: 100%; overflow: hidden; }
  .panel--box   { left: 0;    width: 376px; }
  .panel--zen   { left: 376px; width: 376px; }
  .panel--boost { left: 752px; width: 373px; background: var(--paper); }

  .photo { position: absolute; inset: 0; }
  .photo--office {
    background:
      radial-gradient(ellipse 45% 30% at 45% 28%, #cfc3b7 0%, transparent 100%),
      radial-gradient(ellipse 40% 20% at 50% 68%, #b9aa9b 0%, transparent 100%),
      linear-gradient(90deg, rgba(30,22,18,.55) 0%, transparent 18%, transparent 82%, rgba(30,22,18,.55) 100%),
      linear-gradient(180deg, var(--sepia-mid) 0%, #4a3b31 55%, var(--sepia-dark) 100%);
  }
  .photo--meadow {
    background:
      radial-gradient(ellipse 45% 28% at 45% 26%, #f2efec 0%, transparent 100%),
      radial-gradient(ellipse 30% 10% at 80% 38%, #e6e2de 0%, transparent 100%),
      linear-gradient(180deg, var(--sky-mid) 0%, #a49c95 30%, var(--sky-light) 60%, #8c847c 74%, #3f3731 82%, var(--grass-dark) 100%);
  }

  .top-bar {
    position: absolute; top: 0; height: 8px;
    background: var(--dark-red);
  }
  .panel--box .top-bar   { left: 40px; width: 296px; }
  .panel--zen .top-bar   { left: 40px; width: 296px; }
  .panel--boost .top-bar { left: 40px; width: 295px; }

  .foot-rule {
    position: absolute; top: 499px; height: 1px;
    background: var(--rule-grey);
  }
  .foot-rule::before {
    content: ""; position: absolute; left: 0; top: -1px;
    width: 45px; height: 2px; background: var(--dark-red);
  }
  .panel--box .foot-rule   { left: 15px; width: 365px; opacity: .6; }
  .panel--zen .foot-rule   { left: 30px; width: 340px; opacity: .6; }
  .panel--boost .foot-rule { left: 30px; width: 343px; }

  .headline-box {
    position: absolute; left: 49px; top: 10px;
    font-family: "Open Sans", sans-serif; font-weight: 700;
    font-size: 21px; color: var(--paper);
    text-shadow: 0 1px 3px rgba(0,0,0,.45);
  }

  .thought-cloud {
    position: absolute; left: 21px; top: 16px;
    width: 316px; height: 252px; overflow: visible;
  }
  .cloud-copy {
    position: absolute; left: 22px; top: 72px; width: 314px;
    text-align: center;
    font-family: "Open Sans", sans-serif; font-weight: 400;
    font-size: 25px; line-height: 35.5px;
    color: var(--brand-red);
  }
  .zen-line {
    position: absolute; left: 50px; top: 358px;
    font-family: "Open Sans", sans-serif; font-weight: 400;
    font-size: 25px; color: var(--paper);
    text-shadow: 0 1px 4px rgba(0,0,0,.7);
  }

  .boost-title {
    position: absolute; left: 38px; top: 42px;
    font-family: "Titillium Web", sans-serif; font-weight: 600;
    font-size: 17.5px; color: var(--brand-red);
  }
  .boost-body {
    position: absolute; left: 38px; top: 72px; width: 292px;
    font-family: "Titillium Web", sans-serif; font-weight: 300;
    font-size: 13.4px; line-height: 22.6px; color: var(--body-grey);
  }
  .boost-body p + p { margin-top: 22px; }
  .boost-body em { font-style: italic; }

  .brand-lockup {
    position: absolute; left: 150px; top: 404px; width: 200px;
    text-align: right;
    font-family: "Titillium Web", sans-serif;
  }
  .brand-name {
    font-weight: 700; font-size: 24px; line-height: 26px;
    color: var(--charcoal);
  }
  .brand-rule {
    height: 2px; width: 110px; margin: 6px 0 4px auto;
    background: var(--brand-red);
  }
  .brand-tagline {
    font-weight: 400; font-size: 11px; color: #6e6e6e;
  }
</style>
</head>
<body>
<main class="canvas">
  <section class="spread">

    <article class="panel panel--box">
      <div class="photo photo--office" role="img" aria-label="Sepia photograph of a stressed man in shirt and tie working at a cluttered desk inside a cramped cardboard box, a wall clock above him"></div>
      <div class="top-bar"></div>
      <h2 class="headline-box">Tired of working in a box?</h2>
      <div class="foot-rule"></div>
    </article>

    <article class="panel panel--zen">
      <div class="photo photo--meadow" role="img" aria-label="Sepia photograph of a man lying relaxed in tall grass beneath a wide sky with a large white cloud"></div>
      <div class="top-bar"></div>
      <svg class="thought-cloud" viewBox="-10 -10 316 252" aria-hidden="true">
        <path d="M280 116
                 A38 38 0 0 1 262.3 166
                 A38 38 0 0 1 214 202.6
                 A38 38 0 0 1 148 216
                 A38 38 0 0 1 82 202.6
                 A38 38 0 0 1 33.7 166
                 A38 38 0 0 1 16 116
                 A38 38 0 0 1 33.7 66
                 A38 38 0 0 1 82 29.4
                 A38 38 0 0 1 148 16
                 A38 38 0 0 1 214 29.4
                 A38 38 0 0 1 262.3 66
                 A38 38 0 0 1 280 116 Z"
              fill="none" stroke="#ffffff" stroke-width="1.4"/>
      </svg>
      <p class="cloud-copy">Move<br>your business<br>to cloud powered<br>technologies.</p>
      <p class="zen-line">Zen for your business.</p>
      <div class="foot-rule"></div>
    </article>

    <article class="panel panel--boost">
      <div class="top-bar"></div>
      <h2 class="boost-title">Boost Business with Cloud Computing</h2>
      <div class="boost-body">
        <p>If you are considering cloud technologies for your business, avoid the top three common mistakes. Whether you are looking for IaaS (infrastructure as a service), PaaS (platform as a service), SaaS (software as a service) and considering vendors such as Nimbra, Vastwell or Ledgerpeak.com, we work with you to ensure compliance, security and the greatest benefit to your business.</p>
        <p>We help you significantly reduce the cost of sales and operations, such that you only pay for what you use rather than for what you <em>might</em> need. FIND US IN THE CLOUD.</p>
      </div>
      <div class="brand-lockup">
        <div class="brand-name">Bright-Lane-<br>Webworks</div>
        <div class="brand-rule"></div>
        <div class="brand-tagline">business on skyforge88</div>
      </div>
      <div class="foot-rule"></div>
    </article>

  </section>
</main>
</body>
</html>
```